Walk Bright through the Seasons: 52 Weeks to a Year of Courage and Calm

This is a non-fiction, self-help book. The first edition was published a decade ago, and it needs a new design. Nothing too literal (no actual hearts on the cover) but something inspirational or perhaps something quite plain. The current cover is below for reference, but I DO NOT want something similar to that. It is outdated.

The cover must include:

1. Title: Walk Bright through the Seasons
2. Subtitle: 52 Weeks to a Year of Courage and Calm
3. Author Name: Tobin Wells

It should also have plenty of "white space" in other words the fonts shouldnt be so big that they take up the whole cover.

Dimensions: 9" x 6.25"

Target Market(s)

adults interested in personal development

Font styles to use
Serif
Script

Colors

Designer to choose colors to be used in the design.

Requirements
Must have
• Classic look and feel. The current design is too busy. I have included examples of the style I like below. I'm open to a singular graphic/photo but nothing more than that. Probably plain text is best.
• Please look at the samples I have included of best-selling books in the genre that I like. The cover should be modeled after these.

```html
<!DOCTYPE html>
<html lang="en">
<head>
<meta charset="utf-8">
<title>Walk Bright through the Seasons — Tobin Wells</title>
<link rel="stylesheet" href="https://fonts.googleapis.com/css2?family=Cormorant+Garamond:ital,wght@0,500;0,600;1,500&family=Pinyon+Script&display=swap">
<style>
  :root {
    --paper: #f5f1e8;
    --paper-edge: #ebe5d8;
    --ink: #1f2a3a;
    --ink-soft: #4a5360;
    --gold: #b08a4a;
    --rule: rgba(176, 138, 74, 0.7);
  }
  html, body {
    margin: 0;
    padding: 0;
    width: 934px;
    height: 1200px;
    overflow: hidden;
  }
  .cover {
    position: relative;
    width: 934px;
    height: 1200px;
    background: radial-gradient(ellipse at 50% 45%, var(--paper) 60%, var(--paper-edge) 100%);
    overflow: hidden;
  }
  .title {
    position: absolute;
    left: 0;
    right: 0;
    top: 300px;
    margin: 0;
    text-align: center;
    font-weight: 400;
    line-height: 1;
  }
  .title-line {
    display: block;
  }
  .title-line--first {
    font-family: "Cormorant Garamond", "Garamond", serif;
    font-weight: 500;
    font-size: 62px;
    letter-spacing: 10px;
    text-transform: uppercase;
    color: var(--ink);
    padding-left: 10px;
  }
  .title-line--middle {
    font-family: "Pinyon Script", cursive;
    font-size: 58px;
    color: var(--gold);
    margin-top: 22px;
  }
  .title-line--last {
    font-family: "Cormorant Garamond", "Garamond", serif;
    font-weight: 500;
    font-size: 92px;
    letter-spacing: 14px;
    text-transform: uppercase;
    color: var(--ink);
    margin-top: 18px;
    padding-left: 14px;
  }
  .divider {
    position: absolute;
    left: 50%;
    top: 640px;
    width: 120px;
    height: 12px;
    margin-left: -60px;
  }
  .subtitle {
    position: absolute;
    left: 0;
    right: 0;
    top: 688px;
    margin: 0;
    text-align: center;
    font-family: "Cormorant Garamond", "Garamond", serif;
    font-style: italic;
    font-weight: 500;
    font-size: 28px;
    letter-spacing: 1px;
    color: var(--ink-soft);
  }
  .author {
    position: absolute;
    left: 0;
    right: 0;
    top: 1040px;
    margin: 0;
    text-align: center;
    font-family: "Cormorant Garamond", "Garamond", serif;
    font-weight: 600;
    font-size: 30px;
    letter-spacing: 9px;
    text-transform: uppercase;
    color: var(--ink);
    padding-left: 9px;
  }
</style>
</head>
<body>
  <main class="cover">
    <h1 class="title">
      <span class="title-line title-line--first">Walk Bright</span>
      <span class="title-line title-line--middle">through the</span>
      <span class="title-line title-line--last">Seasons</span>
    </h1>
    <svg class="divider" viewBox="0 0 120 12" aria-hidden="true">
      <line x1="0" y1="6" x2="50" y2="6" stroke="var(--rule)" stroke-width="1"/>
      <circle cx="60" cy="6" r="3" fill="var(--gold)"/>
      <line x1="70" y1="6" x2="120" y2="6" stroke="var(--rule)" stroke-width="1"/>
    </svg>
    <p class="subtitle">52 Weeks to a Year of Courage and Calm</p>
    <p class="author">Tobin Wells</p>
  </main>
</body>
</html>
```